We would like to have 8 Expressions developed for use on our eVigils (online memorials). Visitors to our website will be able to select an Expression and post it to an individual's online memorial.

We will need the files to be developed in Vector format. As per the examples attached the designs should be in a square format (same width as height).

As a guide for minimum text height: no letter (Lower case or capital) should be less than 5% of the overall height of the design (preferably bigger as the designs will be viewed at about 200 x 200 pixels so we don't want a letter smaller than about 10 pixels in height)

Attached are a series of sample designs that you should use as a guide for the type of look/feel we are trying to achieve. We particularly want beautiful fonts/typography. Overall we want a soft feel to the designs.

We don't want the colours to be too dark (other than the blackboard effect) – we would prefer more uplifting colours as displayed in the attachments.

1. Your friendship has been so special to me and life won't be the same without you in it
2. Most amazing person we knew and your constant love and support was never ending
3. You were someone I trusted, someone I could rely on, someone I loved and someone who will be missed
4. Remembering all the great times we spent with you
5. You will be remembered for your gentle nature and generosity of spirit
6. Lived life with courage, love and kindness; all without judgment
7. Generous in spirit, brought joy to family and countless friends
8. You will always hold a special place in our hearts
Updates

Reason: At this stage I haven't received appealing designs so I am extending the deadline in the hope that some new designers are interested in the project. Maeve

Target Market(s)

All different types of ages will place an Expression in memory of someone they have lost.

Industry/Entity Type

Online

Requirements
Must have
• Each of the 5 Expressions have to have a different look/feel to them. Colours need to have a softness about them, expect for 1 which can be a blackboard design.

Essential that the fonts/typography are beautiful and easily readable.
Should not have
• Please don't use dark colours as the expressions are meant to be 'positive' and 'uplifting'.

Don't use boring fonts. Typography is important.

```html
<!DOCTYPE html>
<html lang="en">
<head>
<meta charset="utf-8">
<title>Expression – You Were Someone I Trusted</title>
<link rel="stylesheet" href="https://fonts.googleapis.com/css2?family=Big+Shoulders+Display:wght@500&family=Montserrat:wght@700&display=swap">
<style>
  :root {
    --sand: #F5D097;
    --frame: #FBE6C6;
    --ember: #FF4F0A;
    --cobalt: #1424E8;
  }
  html, body {
    margin: 0;
    padding: 0;
    width: 1200px;
    height: 1200px;
    overflow: hidden;
    background: var(--sand);
  }
  .expression {
    display: block;
    width: 1200px;
    height: 1200px;
  }
  .expression__frame {
    fill: none;
    stroke: var(--frame);
    stroke-width: 2;
  }
  .expression__rule {
    stroke: var(--cobalt);
    stroke-width: 1.5;
  }
  .display {
    font-family: "Big Shoulders Display", "Oswald", sans-serif;
    font-weight: 500;
  }
  .display--ember { fill: var(--ember); }
  .display--cobalt { fill: var(--cobalt); }
  .connector {
    font-family: "Montserrat", sans-serif;
    font-weight: 700;
    fill: var(--cobalt);
  }
</style>
</head>
<body>
<svg class="expression" viewBox="0 0 1200 1200" xmlns="http://www.w3.org/2000/svg" role="img"
     aria-label="You were someone I trusted, someone I could rely on, someone I loved and someone who will be missed">
  <rect width="1200" height="1200" fill="var(--sand)"/>
  <rect class="expression__frame" x="35" y="35" width="1129" height="1129"/>

  <line class="expression__rule" x1="321" y1="195" x2="878" y2="195"/>

  <text class="display display--ember" x="334" y="373" font-size="215"
        textLength="533" lengthAdjust="spacingAndGlyphs">YOU WERE</text>

  <text class="connector" x="349" y="424" font-size="51"
        textLength="501" lengthAdjust="spacingAndGlyphs">SOMEONE I TRUSTED</text>

  <text class="display display--ember" x="426" y="553" font-size="151"
        textLength="350" lengthAdjust="spacingAndGlyphs">SOMEONE</text>

  <text class="connector" x="386" y="604" font-size="49"
        textLength="429" lengthAdjust="spacingAndGlyphs">I COULD RELY ON,</text>

  <text class="display display--ember" x="416" y="730" font-size="150"
        textLength="350" lengthAdjust="spacingAndGlyphs">SOMEONE</text>

  <text class="connector" x="507" y="781" font-size="51"
        textLength="185" lengthAdjust="spacingAndGlyphs">I LOVED</text>

  <text class="display display--ember" x="368" y="885" font-size="132"
        textLength="464" lengthAdjust="spacingAndGlyphs">AND SOMEONE</text>

  <line class="expression__rule" x1="321" y1="898" x2="878" y2="898"/>

  <text class="display display--cobalt" x="326" y="992" font-size="104"
        textLength="545" lengthAdjust="spacingAndGlyphs">WHO WILL BE MISSED</text>

  <line class="expression__rule" x1="321" y1="1008" x2="878" y2="1008"/>
</svg>
</body>
</html>
```